Infographics about Animals

Looking for animal infographics like https://www.instagram.com/cobaltwalrusdoodles/
Could be Animal of the day or perhaps a "know your ..." where we ask for info graphic showing differences in variations of an animal that is often confused (examples: african vs asian elephants, jaguar vs leopard, differences between gibbons, differences between painted dog and spotted hyena, differences between bear species, etc)
Potentially ongoing project for the right freelancer
To start, this proposal will be to output an infographic for Global Pangolin Fortnight and a link Aardvark profile on our website is here: https://critter-atlas.example/listing/aardvark/ where you can get details and fun facts for the infographic
If we move forward, our team will supply some basic ideas or key points to point out in the infographics to help keep your work and just produce the graphic itself.

```html
<!DOCTYPE html>
<html lang="en">
<head>
<meta charset="utf-8">
<title>Global Pangolin Fortnight</title>
<link rel="stylesheet" href="https://fonts.googleapis.com/css2?family=Bitter:wght@400;700;800&family=Kalam:wght@400&family=Montserrat:ital,wght@0,500;0,700;1,500&family=Courier+Prime:wght@700&family=Alfa+Slab+One&display=swap">
<style>
  :root{
    --page:#ffffff;
    --meadow:#7f8f3a;
    --hill-far:#63693f;
    --hill-near:#4f6b1c;
    --lime:#8edb3c;
    --yellow:#eef21e;
    --tan:#e4b867;
    --band-head:#a08058;
    --band-male:#b8905a;
    --band-female:#7a5a48;
    --ink-male:#4a3020;
    --ink-female:#f2a27c;
    --soil:#66503f;
    --fact:#e6ded6;
    --sign:#6f8a2c;
    --coat-light:#b08360;
    --coat-dark:#8c6040;
  }
  *{margin:0;padding:0;box-sizing:border-box}
  html,body{width:1200px;height:1200px;overflow:hidden;background:var(--page)}
  .poster{position:absolute;left:116px;top:136px;width:975px;height:934px;background:var(--soil);overflow:hidden}
  .scene{position:absolute;left:0;top:0;width:975px;height:438px;background:var(--meadow);overflow:hidden}
  .scene .landscape{position:absolute;left:0;top:0;width:975px;height:438px}
  .scene .ridge-text{position:absolute;left:0;top:0;width:975px;height:438px;z-index:3}
  .scene .animal{position:absolute;left:265px;top:236px;width:488px;height:180px;border-radius:46% 50% 34% 40%;background:radial-gradient(ellipse at 55% 40%,var(--coat-light),var(--coat-dark));z-index:2}
  .title{position:absolute;left:0;top:30px;width:975px;text-align:center;font-family:'Bitter',serif;font-weight:800;font-size:50px;color:var(--lime);letter-spacing:.5px;z-index:4}
  .title .accent{color:var(--yellow)}
  .sign{position:absolute;left:52px;top:174px;width:208px;height:108px;background:var(--sign);transform:rotate(-11deg);box-shadow:-6px 8px 14px rgba(0,0,0,.35);z-index:4}
  .sign-text{position:absolute;left:74px;top:172px;transform:rotate(-16deg);font-family:'Bitter',serif;line-height:1;z-index:5}
  .sign-text .did{display:block;color:var(--lime);font-weight:700;font-size:36px}
  .sign-text .know{display:block;color:var(--yellow);font-weight:800;font-size:42px;margin-left:8px}
  .sign-q{position:absolute;left:212px;top:148px;font-family:'Bitter',serif;font-weight:800;font-size:80px;line-height:1;color:#fff;transform:rotate(-8deg);z-index:5}
  .native{position:absolute;left:720px;top:128px;transform:rotate(14deg);text-align:center;line-height:1;z-index:4}
  .native .lead{display:block;font-family:'Courier Prime',monospace;font-weight:700;font-size:30px;color:var(--tan);letter-spacing:2px}
  .native .land{display:block;font-family:'Alfa Slab One',serif;font-size:44px;color:#d8e82a;letter-spacing:2px}
  .native .region{display:block;font-family:'Courier Prime',monospace;font-weight:700;font-size:27px;color:var(--tan);letter-spacing:1px}
  .sizes{position:absolute;left:0;top:438px;width:975px;font-family:'Montserrat',sans-serif;font-weight:500;font-size:17px}
  .sizes .row{display:grid;grid-template-columns:163px 236px 266px 260px 50px;align-items:center}
  .sizes .head{height:30px;background:var(--band-head);font-family:'Bitter',serif;font-weight:400;font-size:18px;color:#fff}
  .sizes .male{height:30px;background:var(--band-male);color:var(--ink-male)}
  .sizes .female{height:31px;background:var(--band-female);color:var(--ink-female);border-top:1px solid #8a6a50}
  .sizes .label{padding-left:23px;white-space:nowrap}
  .sizes .cell{text-align:center;white-space:nowrap}
  .facts{position:absolute;left:37px;top:552px;list-style:none;font-family:'Montserrat',sans-serif;font-style:italic;font-weight:500;font-size:20.5px;color:var(--fact);letter-spacing:.3px}
  .facts li{height:35px;line-height:35px;white-space:nowrap}
  .link{position:absolute;left:24px;top:890px;font-family:'Bitter',serif;font-weight:400;font-size:18px;color:var(--yellow)}
  .brand{position:absolute;left:740px;top:886px;display:flex;align-items:center;gap:10px;font-family:'Montserrat',sans-serif;font-weight:700;font-size:26px;color:var(--yellow)}
  .brand .dot{width:20px;height:20px;border-radius:50%;background:var(--yellow)}
</style>
</head>
<body>
<main class="poster">
  <section class="scene">
    <svg class="landscape" width="975" height="438" viewBox="0 0 975 438">
      <path d="M0,190 C60,170 120,165 175,200 C220,230 260,260 300,290 L0,330 Z" fill="var(--hill-far)"/>
      <path d="M780,330 C840,290 870,262 905,262 C940,262 960,275 975,285 L975,360 Z" fill="var(--hill-far)"/>
      <path d="M0,389 C150,350 320,230 420,175 C480,145 560,140 620,170 C720,220 850,340 975,382 L975,438 L0,438 Z" fill="var(--hill-near)"/>
      <ellipse cx="522" cy="418" rx="230" ry="12" fill="rgba(40,40,10,.45)"/>
    </svg>
    <div class="animal" role="img" aria-label="Illustration of a walking aardvark in side view, facing left"></div>
    <svg class="ridge-text" width="975" height="438" viewBox="0 0 975 438">
      <defs>
        <path id="ridge" d="M20,418 C150,382 320,262 420,206 C480,176 560,170 620,198 C720,248 850,356 975,420"/>
      </defs>
      <text font-family="Kalam, cursive" font-size="24">
        <textPath href="#ridge" startOffset="0"><tspan fill="var(--yellow)">Top Speed: </tspan><tspan fill="#fff">25 mph </tspan><tspan fill="var(--lime)">(40 km/h)</tspan></textPath>
      </text>
      <text font-family="Kalam, cursive" font-size="23">
        <textPath href="#ridge" startOffset="420"><tspan fill="var(--yellow)">Lifespan:  </tspan><tspan fill="#fff">18 Years </tspan><tspan fill="var(--lime)">(wild) </tspan><tspan fill="var(--yellow)"> // </tspan><tspan fill="#fff"> 25 Years </tspan><tspan fill="var(--lime)">(caaptivity)</tspan></textPath>
      </text>
    </svg>
    <h1 class="title">Global <span class="accent">Pangolin</span> Fortnight</h1>
    <div class="sign"></div>
    <p class="sign-text"><span class="did">Did You</span><span class="know">KNOW</span></p>
    <span class="sign-q">?</span>
    <p class="native"><span class="lead">Native to</span><span class="land">AFRICA</span><span class="region">(sub-Saharan)</span></p>
  </section>

  <section class="sizes">
    <div class="row head"><span></span><span class="cell">LENGTH</span><span class="cell">HEIGHT</span><span class="cell">WEIGHT</span><span></span></div>
    <div class="row male"><span class="label">MALE (Boar)</span><span class="cell">43-53 inches (109-135 cm)</span><span class="cell">43-53 inches (109-135 cm)</span><span class="cell">43-53 inches (109-135 cm)</span><span></span></div>
    <div class="row female"><span class="label">FEMALE (Sow)</span><span class="cell">39-49 inches (99-125 cm)</span><span class="cell">39-49 inches (99-125 cm)</span><span class="cell">39-49 inches (99-125 cm)</span><span></span></div>
  </section>

  <ul class="facts">
    <li>"Aardvark" originates from the Afrikaans word for "earth pig."</li>
    <li>Aardvarks have a keen sense of hearing, which they use to detect predators.</li>
    <li>They have very poor eyesight and rely heavily on their sense of smell and hearing.</li>
    <li>The Aardvark can dig a burrow in less than 5 minutes.</li>
    <li>They can close their nostrils to prevent sand from entering while digging.</li>
    <li>They can eat up to 50,000 ants or termites in a single night.</li>
    <li>It has a tongue that can extend up to 12 inches.</li>
    <li>An Aardvark's thick skin protects it from being bitten by ants.</li>
    <li>Aardvarks are good swimmers and can cross rivers if needed.</li>
  </ul>

  <p class="link">https://critter-atlas.example/listing/aardvark/</p>
  <p class="brand"><span class="dot"></span>Critter Atlas</p>
</main>
</body>
</html>
```